Business Card Design

i am looking a business card for a car rental company long with Taxi service also a logo.

what is the latest with my project

Industry/Entity Type

Business

Contact Information for Business Card

name of the Company is Kestrel Bay Motor Leasing and Taxi Services
Address: Linden Cove Village, St. Agnes's Parish Antigua
Tele# 555-0142/5550187-555-0163
Email: lorimbeck@quillmarsh.test

Font styles to use
Script

```html
<!DOCTYPE html>
<html lang="en">
<head>
<meta charset="utf-8">
<title>Kestrel Bay Motor Leasing and Taxi Services – Business Card</title>
<link rel="stylesheet" href="https://fonts.googleapis.com/css2?family=Arimo:wght@400&family=Pinyon+Script&display=swap">
<style>
  :root {
    --band-light: #5b5aa2;
    --band-mid: #3b3a85;
    --band-dark: #29286a;
    --strip: #ffffff;
    --photo-light: #eceef2;
    --photo-dark: #b9bcc4;
    --ink-light: #ffffff;
  }
  * { margin: 0; padding: 0; box-sizing: border-box; }
  html, body {
    width: 1200px;
    height: 675px;
    overflow: hidden;
    background: #ffffff;
  }
  .card {
    position: relative;
    width: 1200px;
    height: 675px;
    overflow: hidden;
    font-family: "Arimo", Arial, sans-serif;
    color: var(--ink-light);
  }
  .card__header {
    position: absolute;
    left: 0; top: 0;
    width: 100%;
    height: 166px;
    background: linear-gradient(100deg, var(--band-light) 0%, var(--band-mid) 45%, var(--band-dark) 100%);
  }
  .card__title {
    position: absolute;
    left: 40px; right: 40px;
    top: 50px;
    text-align: center;
    font-family: "Pinyon Script", cursive;
    font-size: 58px;
    line-height: 1;
    font-weight: 400;
    white-space: nowrap;
  }
  .card__fleet {
    position: absolute;
    left: 0; top: 166px;
    width: 100%;
    height: 277px;
    background: var(--strip);
  }
  .card__fleet-photo {
    position: absolute;
    left: 61px; top: 56px;
    width: 1090px;
    height: 190px;
    border-radius: 14px;
    background: linear-gradient(180deg, var(--photo-light) 0%, var(--photo-dark) 100%);
  }
  .card__footer {
    position: absolute;
    left: 0; top: 443px;
    width: 100%;
    height: 232px;
    background: linear-gradient(100deg, var(--band-mid) 0%, var(--band-dark) 100%);
  }
  .contact {
    position: absolute;
    right: 675px;
    top: 64px;
    text-align: right;
    font-style: normal;
    font-size: 31px;
    line-height: 37px;
    white-space: nowrap;
  }
  .divider {
    position: absolute;
    left: 564px;
    top: 66px;
    width: 2px;
    height: 110px;
    background: var(--ink-light);
  }
  .address {
    position: absolute;
    left: 600px;
    top: 65px;
    font-size: 34px;
    line-height: 54px;
    white-space: nowrap;
  }
</style>
</head>
<body>
  <main class="card">
    <header class="card__header">
      <h1 class="card__title">Kestrel Bay Motor Leasing and Taxi Services</h1>
    </header>

    <section class="card__fleet">
      <div class="card__fleet-photo" role="img" aria-label="Photo of the rental fleet: a yellow taxi, a silver sedan, a black luxury sedan and a grey minivan"></div>
    </section>

    <footer class="card__footer">
      <address class="contact">
        <div class="contact__phone">555-0142/5550</div>
        <div class="contact__phone">187-555-0163</div>
        <div class="contact__email">lorimbeck@quillmarsh.test</div>
      </address>
      <div class="divider"></div>
      <p class="address">Linden Cove Village, St.<br>Agnes's Parish Antigua</p>
    </footer>
  </main>
</body>
</html>
```